WBL Kids Choir

Card to hand out or mail out with our own mailing labels. Needs to be appealing to families with children ages 4 yrs through 6th grade, who have an interest in musical experiences for the kids in a contemporary Bible teaching/church setting. We have 3 different kids choirs: 4-yr-old & Kindergarten Choir, 1st-3rd grade choir, and 4th-6th grade choir. This is a FREE after-school program every Tuesday from 3:30-5:00. Transportation for grades 1-6 from local schools is provided. Parents should expect their children to experience fun, friends, music, recreation, games, snacks, character building, Bible teaching, in an encouraging church environment.

Industry/Entity Type

Church

Requirements
Nice to have
• Bight colors

```html
<!DOCTYPE html>
<html lang="en">
<head>
<meta charset="utf-8">
<title>WBL Kids Choir</title>
<link rel="stylesheet" href="https://fonts.googleapis.com/css2?family=Graduate&family=Squada+One&family=Kalam:wght@400&family=Bowlby+One+SC&family=Luckiest+Guy&family=Lilita+One&family=Caveat:wght@500&display=swap">
<style>
  :root {
    --paper: #faf6ee;
    --green: #7dc242;
    --green-band: #7cc143;
    --outline-red: #e8383d;
    --orange: #f6921e;
    --olive: #8c9a3c;
    --pink-deep: #e2345c;
    --pink-soft: #ee5f7d;
    --blue: #2a7cc7;
    --ink: #2b2b2b;
    --white: #ffffff;
    --script-red: #e8262d;
  }
  * { margin: 0; padding: 0; box-sizing: border-box; }
  html, body { width: 1000px; height: 1200px; overflow: hidden; background: var(--paper); }
  .flyer { position: relative; width: 1000px; height: 1200px; background: var(--paper); overflow: hidden; }

  .notes-art {
    position: absolute; left: 0; top: 0; width: 400px; height: 1200px;
    background:
      radial-gradient(ellipse 160px 220px at 120px 180px, rgba(125,194,66,.55), transparent 70%),
      radial-gradient(ellipse 150px 200px at 270px 260px, rgba(246,196,30,.5), transparent 70%),
      radial-gradient(ellipse 140px 200px at 110px 480px, rgba(246,146,30,.45), transparent 70%),
      radial-gradient(ellipse 160px 220px at 280px 560px, rgba(232,56,61,.4), transparent 70%),
      radial-gradient(ellipse 150px 200px at 140px 780px, rgba(125,194,66,.45), transparent 70%),
      radial-gradient(ellipse 140px 200px at 260px 900px, rgba(42,124,199,.35), transparent 70%),
      linear-gradient(90deg, #f1eee6 0%, #f6f3ec 80%, rgba(250,246,238,0) 100%);
  }

  .title { position: absolute; left: 380px; width: 520px; text-align: center; color: var(--green);
    -webkit-text-stroke: 1.5px var(--outline-red); paint-order: stroke fill; }
  .title-initials { top: 48px; font: 150px/1 "Graduate", serif; letter-spacing: 2px; }
  .title-name { top: 222px; font: 132px/1 "Squada One", sans-serif; letter-spacing: 4px; }

  .choir-list-shape { position: absolute; left: 365px; top: 374px; width: 535px; height: 286px; }
  .choir-list { position: absolute; left: 405px; top: 408px; width: 480px; color: var(--ink);
    font-family: "Kalam", cursive; }
  .choir-list h2 { font-weight: 400; font-size: 38px; line-height: 1.2; text-align: center; margin-bottom: 14px; }
  .choir-list li { list-style: none; font-size: 29px; line-height: 1.55; }

  .program-label { position: absolute; left: 350px; top: 683px; width: 590px; text-align: center;
    font: 33px/1 "Bowlby One SC", sans-serif; color: var(--green); letter-spacing: 1px; }

  .schedule-shape { position: absolute; left: 420px; top: 752px; width: 406px; height: 140px; }
  .schedule { position: absolute; left: 420px; top: 776px; width: 406px; text-align: center; color: var(--white);
    font-family: "Luckiest Guy", sans-serif; }
  .schedule-day { font-size: 31px; line-height: 1.1; }
  .schedule-time { font-size: 50px; line-height: 1.1; }

  .transport { position: absolute; left: 380px; top: 914px; width: 590px; text-align: center;
    font: 30px/1.25 "Lilita One", sans-serif; color: var(--blue); }

  .dots-border { position: absolute; left: 0; top: 1024px; width: 1000px; height: 40px;
    background: repeating-linear-gradient(90deg, #f5c61e 0 42px, #e8383d 42px 84px, #7dc242 84px 126px, #62c3c6 126px 168px);
    opacity: .75; }
  .benefits-band { position: absolute; left: 0; top: 1064px; width: 1000px; height: 88px; background: var(--green-band); }
  .benefits { position: absolute; left: 0; top: 6px; width: 1000px; text-align: center;
    font: 500 27px/1.12 "Caveat", cursive; color: var(--script-red); }
  .benefits-dots { position: absolute; left: 6px; right: 6px; bottom: 8px; border-bottom: 8px dotted var(--white); }
</style>
</head>
<body>
<main class="flyer">
  <div class="notes-art" role="img" aria-label="Colourful cascade of musical notes, treble and bass clefs in green, yellow, orange, red and blue"></div>

  <h1>
    <span class="title title-initials">WBL</span>
    <span class="title title-name">KIDS CHOIR</span>
  </h1>

  <svg class="choir-list-shape" viewBox="0 0 535 286" aria-hidden="true">
    <path d="M34 3 H501 A31 31 0 0 0 532 34 V252 A31 31 0 0 0 501 283 H34 A31 31 0 0 0 3 252 V34 A31 31 0 0 0 34 3 Z"
          fill="var(--orange)" stroke="var(--olive)" stroke-width="6"/>
    <path d="M40 14 H495 A27 27 0 0 0 521 40 V246 A27 27 0 0 0 495 272 H40 A27 27 0 0 0 14 246 V40 A27 27 0 0 0 40 14 Z"
          fill="none" stroke="#fbe3b8" stroke-width="2" stroke-dasharray="6 5"/>
  </svg>
  <section class="choir-list">
    <h2>Three different kids choirs:</h2>
    <ol>
      <li>1) 4-yr-old &amp; Kindergarten Choir</li>
      <li>2) 1st-3rd grade choir</li>
      <li>3) 4th-6th grade choir</li>
    </ol>
  </section>

  <p class="program-label">FREE AFTER–SCHOOL PROGRAM</p>

  <svg class="schedule-shape" viewBox="0 0 406 140" aria-hidden="true">
    <path d="M22 2 H384 A20 20 0 0 0 404 22 V118 A20 20 0 0 0 384 138 H22 A20 20 0 0 0 2 118 V22 A20 20 0 0 0 22 2 Z"
          fill="var(--pink-deep)"/>
    <rect x="20" y="16" width="366" height="108" rx="22" fill="var(--pink-soft)"/>
    <line x1="70" y1="24" x2="336" y2="24" stroke="#fff" stroke-opacity=".6" stroke-width="3" stroke-dasharray="3 3"/>
    <line x1="70" y1="116" x2="336" y2="116" stroke="#fff" stroke-opacity=".6" stroke-width="3" stroke-dasharray="3 3"/>
  </svg>
  <div class="schedule">
    <p class="schedule-day">every Tuesday from:</p>
    <p class="schedule-time">3:30-5:00</p>
  </div>

  <p class="transport">Transportation for grades 1-6<br>from local schools IS PROVIDED!!!</p>

  <div class="dots-border" role="img" aria-label="Decorative row of colourful polka dots"></div>
  <footer class="benefits-band">
    <p class="benefits">Experience Fun, Friends, Music, Recreation, Games, Snacks,<br>Character Building, Bible Teaching, In An Encouraging Church Environment.</p>
    <div class="benefits-dots"></div>
  </footer>
</main>
</body>
</html>
```